Website Design - for Energy Efficiency company - large corporate feel

Hi there,
Thanks for checking out this project!
We're a UK based energy efficiency business. We arrange for energy efficient systems to be fitted in people's houses (i.e. efficient boilers, solar panels etc.) However, we do not install them ourselves as we have accredited installers who install on our behalf. Therefore the website should appeal to these businesses and have a very professional corporate feel. The final design should communicate that we are a financially safe large corporation.
Our existing website should not be used for inspiration as the style and content are very outdated (it was from a time when were installers - which we no longer are).
The new website design should use the greens from our logo, however I don't want the site saturated in this colour.
I'm really open to your chosen layout and therefore I'm not a huge fan of including links to websites I like - as I don't want to limit your own creativity. However, I would like it to look corporate (but not too boring and unimaginative).
So here's a few links to websites that I feel give a feel of financially safe / large corporate etc. Although you certainly don't have to design with this style / layout in mind:
http://www.brenholt.org.uk/advice
http://www.tavishworks.co.uk/
http://www.dqvb.org.uk/
http://www.orrinlodgeway.co.uk/
http://www.pkwynd.co.uk/ (very bad design but looks corporate)
http://www.ferrowmoor.org.uk/
http://www.tq.co.uk/ (looks corporate but too busy and boring)
http://www.quellaro.co.uk/business/index.htm
http://www.mobrevo.com/
https://www.tervold.com/en/index.html
The site is for 4 different audiences:
Consumers | Businesses | Public Sector | Installers
Therefore, it's important that there is some form of way of splitting the site up into these sections (almost like 4 websites in 1). Each section will then have the navigation menu with 7 links.
I've attached our logo (company-logo.jpg) and another logo design we have to display inline with regulations (fair-loan-logo.jpg).
Happy designing, and thank you!

```html
<!DOCTYPE html>
<html lang="en">
<head>
<meta charset="utf-8">
<title>Verdimo Energy – Home</title>
<link rel="stylesheet" href="https://fonts.googleapis.com/css2?family=Open+Sans:ital,wght@0,300;0,400;0,600;0,700;0,800;1,300&display=swap">
<style>
:root{
  --green:#7ab929;
  --green-dark:#4f8a1c;
  --green-text:#3f7d14;
  --sky-top:#3a7fe0;
  --sky-bottom:#ffffff;
  --page:#ffffff;
  --nav-bg:#ececec;
  --band-bg:#ececec;
  --card-border:#d4d4d4;
  --dark-btn:#4a4a4a;
  --text:#333333;
  --muted:#6b6b6b;
  --hero-a:#6f9f92;
  --hero-b:#bfd6d0;
  --footer:#111111;
  --footer-bar:#2b2b2b;
  --footer-text:#9a9a9a;
}
*{box-sizing:border-box;margin:0;padding:0}
html,body{width:1200px;height:1200px;overflow:hidden}
body{font-family:"Open Sans",Arial,sans-serif;color:var(--text);
  background:linear-gradient(180deg,var(--sky-top) 0%,#8fb8ef 30%,#dfe9f7 50%,var(--sky-bottom) 62%);position:relative}
.page{position:absolute;left:163px;top:0;width:874px;height:1050px;background:var(--page)}
.abs{position:absolute}

.brand{left:46px;top:40px;display:flex;align-items:center;gap:10px}
.brand-dot{width:44px;height:44px;border-radius:50%;background:var(--green)}
.brand-name{font-size:33px;font-weight:600;color:var(--green-dark);letter-spacing:-.5px}
.contact{left:470px;top:50px;text-align:center;font-size:13.5px;font-weight:600;color:var(--green-text);line-height:21px;width:220px}
.badge{left:754px;top:12px;width:80px;height:87px;background:var(--green-dark);border-radius:3px}

.nav{left:17px;top:140px;width:840px;height:40px;background:var(--nav-bg);border-bottom:4px solid var(--green);display:flex}
.nav a{font-size:17px;color:#333;text-decoration:none;line-height:36px;text-align:center}
.nav a.active{background:var(--green);color:#fff}

.hero{left:17px;top:190px;width:840px;height:308px;
  background:linear-gradient(90deg,var(--hero-a) 0%,#8fb5aa 55%,var(--hero-b) 100%)}
.hero h1{position:absolute;left:36px;top:28px;font-size:58px;font-weight:800;color:#263130;letter-spacing:.5px}
.hero .sub{position:absolute;left:36px;top:96px;font-size:46px;font-weight:300;color:#263130;line-height:52px}
.hero .sub em{font-style:italic}
.boiler{position:absolute;left:590px;top:12px;width:200px;height:278px;border-radius:6px;
  background:linear-gradient(180deg,#dfe6e4,#c4ceca)}
.dots{position:absolute;left:13px;top:284px;display:flex;gap:13px}
.dots span{width:13px;height:13px;border-radius:50%;background:#a8c6be}
.dots span.on{background:#fff}

.band{left:17px;top:507px;width:840px;height:84px;background:var(--band-bg)}
.band p{position:absolute;left:14px;top:5px;font-size:26px;font-weight:400;color:#111;line-height:38px}
.quote-btn{position:absolute;left:614px;top:20px;width:206px;height:47px;border-radius:4px;
  background:linear-gradient(180deg,#8cc63f,#5e9e1f);color:#fff;font-size:17px;font-weight:700;text-align:center;line-height:47px}

.audiences{left:17px;top:606px;width:840px;height:114px;display:flex;gap:16px}
.card{flex:1;border:1px solid var(--card-border);background:linear-gradient(180deg,#fff,#f0f0f0);text-align:center}
.card h2{font-size:33px;font-weight:300;color:#333;margin-top:8px;line-height:44px}
.card .call{display:inline-flex;align-items:center;gap:10px;margin-top:12px;height:34px;padding:0 14px;
  background:var(--dark-btn);color:#fff;font-size:15px;font-weight:700;border-radius:2px}
.card.active{background:linear-gradient(180deg,#80bd33,#4f8e1c);border-color:#4a8118}
.card.active h2{color:#fff}
.card.active .call{background:#fff;color:var(--green-dark)}

.copy{left:17px;top:742px;width:620px;font-size:11.2px;line-height:17px;text-align:justify;color:#222}
.copy p{margin-bottom:17px}
.photo{left:652px;top:746px;width:205px;height:198px;background:linear-gradient(180deg,#8b7a6a 0%,#6d7f95 45%,#3e5577 100%)}

.footer{left:0;top:1050px;width:1200px;height:114px;background:var(--footer)}
.footer-links{position:absolute;left:198px;top:12px;display:grid;grid-template-columns:121px 100px;font-size:13px;line-height:21px;color:var(--footer-text)}
.footer-contact{position:absolute;left:518px;top:14px;display:flex;gap:14px;align-items:flex-start}
.footer-contact div{font-size:13.5px;line-height:26px;color:#c8c8c8}
.footer-about{position:absolute;left:854px;top:14px;display:flex;gap:24px}
.footer-about p{font-size:13px;line-height:19px;color:var(--footer-text);width:95px}
.bottom-bar{left:0;top:1164px;width:1200px;height:36px;background:var(--footer-bar);text-align:center;font-size:10.5px;line-height:36px;color:#aaa}
</style>
</head>
<body>
<div class="page">
  <div class="abs brand"><span class="brand-dot"></span><span class="brand-name">Verdimo Energy</span></div>
  <div class="abs contact">Tel: (020) 555 018 2047<br>Email: info@verdimo.co.uk</div>
  <div class="abs badge" role="img" aria-label="Approved scheme badge"></div>

  <nav class="abs nav">
    <a class="active" href="#" style="width:85px">Home</a>
    <a href="#" style="width:103px">About Us</a>
    <a href="#" style="width:127px">Fair Loan</a>
    <a href="#" style="width:80px">ECO</a>
    <a href="#" style="width:127px">Landlords</a>
    <a href="#" style="width:137px">Renewables</a>
    <a href="#" style="width:181px">Contact Us</a>
  </nav>

  <section class="abs hero">
    <h1>FREE BOILER</h1>
    <div class="sub">Installed under the<br><em>'ECO Scheme'</em></div>
    <div class="boiler" role="img" aria-label="Wall-mounted white combination boiler"></div>
    <div class="dots"><span class="on"></span><span></span><span></span></div>
  </section>

  <section class="abs band">
    <p>Lorem ipsum dolor sit amet, consectetuer<br>Aenean massa. Cum sociis natoque p</p>
    <div class="quote-btn">GET A FREE QUOTE</div>
  </section>

  <section class="abs audiences">
    <div class="card active"><h2>Consumers</h2><span class="call">CALL US NOW
      <svg width="12" height="16" viewBox="0 0 12 16"><path d="M2 1l8 7-8 7" fill="none" stroke="currentColor" stroke-width="3"/></svg></span></div>
    <div class="card"><h2>Businesses</h2><span class="call">CALL US NOW
      <svg width="12" height="16" viewBox="0 0 12 16"><path d="M2 1l8 7-8 7" fill="none" stroke="currentColor" stroke-width="3"/></svg></span></div>
    <div class="card"><h2>Public Sector</h2><span class="call">CALL US NOW
      <svg width="12" height="16" viewBox="0 0 12 16"><path d="M2 1l8 7-8 7" fill="none" stroke="currentColor" stroke-width="3"/></svg></span></div>
    <div class="card"><h2>Installers</h2><span class="call">CALL US NOW
      <svg width="12" height="16" viewBox="0 0 12 16"><path d="M2 1l8 7-8 7" fill="none" stroke="currentColor" stroke-width="3"/></svg></span></div>
  </section>

  <article class="abs copy">
    <p>Lorem ipsum dolor sit amet, consectetuer adipiscing elit. Aenean commLorem ipsum dolor sit amet, consectetuer adipiscing elit. Aenean commodo ligula eget dolor. Aenean massa. Cum sociis natoLorem ipsum dolor sit amet, consectetuer adipiscing elit. Aenean commLorem ipsum dolor sit amet, consectetuer adipiscing elit. Aenean commodo ligula eget dolor. Aenean massa. Cum sociis natoque penatibus et magnis dis parturient montes, nascetur ridiculus mus. Donec quam felis, ultricies nec, pellentesque eu, pretium quis, sem.</p>
    <p>Nulla consequat massa quis enim. Donec pede justo, fringilla vel, aliquet nec,Nulla consequat massa quis enim. Donec pede justo, fringilla vel, aliquet nec, vulputate eget, arcu.odo ligula eget dolor.  vulputate eget, arcu.odo ligula eget dolor. Aenean massa. Cum sociis natoque penatibus et magnis dis parturient montes, nascetur</p>
    <p>Donec pede justo, fringilla vel, aliquet nec, vulputate eget, arcu.que penatibus et magnis dis parturient montes, nascetur ridiculus mus. Donec quam felis, ultricies nec, pellentesque eu, pretium quis, sem. Nulla consequat massa quis enim. Donec pede justo,</p>
  </article>
  <div class="abs photo" role="img" aria-label="Installer fitting solar panels on a flat roof"></div>
</div>

<footer class="abs footer">
  <div class="footer-links">
    <span>Home</span><span>ECO</span>
    <span>About Us</span><span>Landlords</span>
    <span>Fair Loan</span><span>Renewables</span>
  </div>
  <div class="footer-contact">
    <svg width="46" height="46" viewBox="0 0 46 46" aria-hidden="true">
      <circle cx="23" cy="23" r="21" fill="none" stroke="#9a9a9a" stroke-width="2.5"/>
      <path d="M17 12c-3 1-4 4-3 8 2 6 6 11 12 14 3 1 5 0 6-2l-4-5-3 2c-2-1-5-5-5-7l2-3z" fill="#9a9a9a"/>
    </svg>
    <div>Tel: (020) 555 018 2047<br>Email: info@verdimo.co.uk</div>
  </div>
  <div class="footer-about">
    <svg width="56" height="52" viewBox="0 0 56 52" aria-hidden="true">
      <path d="M28 4a11 11 0 0 0-11 11c0 8 11 20 11 20s11-12 11-20A11 11 0 0 0 28 4z" fill="#9a9a9a"/>
      <circle cx="28" cy="15" r="4.5" fill="#111"/>
      <path d="M12 32l-8 16h48l-8-16h-8M12 32h8M4 48l18-8 12 8" fill="none" stroke="#9a9a9a" stroke-width="2.5"/>
    </svg>
    <p>Lorem ipsum dolor sit amet, consectetuer a dipiscing elit.</p>
  </div>
</footer>
<div class="abs bottom-bar">Copyright 2013 Verdimo &nbsp;| All Rights Reserved</div>
</body>
</html>
```